lab equipment website

We need a fresh new look for a company website called tarvio. We will be using the current logo and brand colors on their current website tarvio.com. They want to keep their text and on-page SEO, but would like to reformat it to look more modern and fresh. They want to have everything be high performance with a great user experience. Their main call to action is for people to fill in a contact form so they can call them. There is some information that is purposely above the fold on the instrument pages. I will need the home page, about page and a leasing page.

```html
<!DOCTYPE html>
<html lang="en">
<head>
<meta charset="utf-8">
<title>tarvio — Lab Equipment Leasing</title>
<link href="https://fonts.googleapis.com/css2?family=Montserrat:wght@400;500;600;700&family=Open+Sans:wght@400;600&display=swap" rel="stylesheet">
<style>
:root{
  --navy:#0c2756;
  --navy-deep:#081a3a;
  --teal:#22c7a4;
  --teal-dark:#0f3f44;
  --yellow:#f6d80a;
  --charcoal:#1f2226;
  --skills:#24272c;
  --white:#ffffff;
  --ink:#1d1f22;
  --muted:#8d9299;
  --line:#d8dadd;
  --green:#3fae5a;
  --blue:#2fa8e0;
  --orange:#f39a1e;
  --footer:#3a3d42;
}
*{box-sizing:border-box;margin:0;padding:0}
html,body{width:1200px;height:4358px;overflow:hidden}
body{font-family:"Open Sans",Arial,sans-serif;color:var(--ink);background:var(--white);position:relative}
h1,h2,h3,h4,.nav,.btn,.link{font-family:"Montserrat",Arial,sans-serif}
section,header,footer{position:relative;width:1200px;overflow:hidden}
.abs{position:absolute}

/* hero */
.hero{height:581px;background:linear-gradient(120deg,#0a2150 0%,#10306a 55%,#0a2150 100%)}
.brand{left:85px;top:24px;display:flex;align-items:center;gap:10px;color:var(--white)}
.brand-dot{width:30px;height:30px;border-radius:50%;background:var(--teal)}
.brand-name{font-family:"Montserrat",sans-serif;font-weight:700;font-size:30px;letter-spacing:.5px}
.nav{left:555px;top:34px;display:flex;gap:34px;font-size:13px;font-weight:600;color:var(--white);letter-spacing:.5px}
.nav-phone{left:978px;top:27px;display:flex;align-items:center;gap:12px;color:var(--white);font-family:"Montserrat",sans-serif;font-size:14px;font-weight:600}
.nav-phone .ic{width:28px;height:28px;border-radius:50%;background:var(--teal);display:flex;align-items:center;justify-content:center}
.hero-title{left:85px;top:200px;font-size:44px;line-height:60px;font-weight:700;color:var(--white)}
.hero-title span{color:var(--teal);display:block}
.hero-more{left:85px;top:424px;font-size:14px;font-weight:700;color:var(--white);border-bottom:2px solid var(--white);padding-bottom:4px}
.hero-pager{left:85px;top:490px;font-size:11px;color:var(--white);display:flex;align-items:center;gap:10px;font-family:"Montserrat",sans-serif;font-weight:600}
.hero-frame{left:815px;top:138px;width:236px;height:312px;border:10px solid var(--teal)}
.hero-product{left:700px;top:120px;width:300px;height:330px;border-radius:40px 40px 70px 70px;background:linear-gradient(160deg,#f2f3f5,#b9bdc4)}

/* contact bar */
.contact-bar{height:102px;background:var(--navy-deep);display:flex;align-items:center;padding-left:85px}
.contact-bar label{font-family:"Montserrat",sans-serif;color:var(--white);font-size:16px;font-weight:500;width:120px}
.bar-field{width:240px;height:40px;border:1px solid #7f8aa0;color:#c7ccd6;font-size:12px;padding:12px 10px;margin-right:20px}
.btn{display:inline-flex;align-items:center;justify-content:center;font-weight:700;font-size:13px}
.btn-yellow{background:var(--yellow);color:var(--ink);width:140px;height:40px}

/* trusted */
.trusted{height:459px}
.trusted-band{left:775px;top:0;width:155px;height:459px;background:var(--teal)}
.trusted-photo{left:672px;top:82px;width:438px;height:290px;background:linear-gradient(135deg,#dfe3ea,#7b8699 60%,#3c4657);box-shadow:0 8px 20px rgba(0,0,0,.25)}
.trusted h2{left:85px;top:80px;width:560px;font-size:30px;line-height:42px;font-weight:700}
.teal-text{color:var(--teal)}
.trusted p{left:85px;top:222px;width:540px;font-size:13px;line-height:22px;color:#4a4e55}
.link{font-size:13px;font-weight:700;border-bottom:2px solid currentColor;padding-bottom:4px}
.trusted .link{left:85px;top:380px}

/* understand */
.understand{height:601px;background:var(--charcoal);color:var(--white)}
.donut{left:120px;top:55px}
.understand h2{left:610px;top:80px;font-size:29px;line-height:40px;font-weight:700;width:520px}
.understand p{left:610px;top:180px;width:500px;font-size:12.5px;line-height:21px;color:#d7d9dc}
.checks{left:610px;top:258px;width:520px;list-style:none;font-size:12.5px;line-height:19px;color:#e5e7ea}
.checks li{display:flex;gap:14px;margin-bottom:16px}
.checks svg{flex:none;margin-top:3px}
.understand .link{left:610px;top:490px;color:var(--white);border:none}

/* cta */
.cta{height:81px;background:var(--teal);display:flex;align-items:center;justify-content:space-between;padding:0 90px 0 85px;color:var(--white);font-size:18px}

/* features */
.features{height:355px;display:flex;justify-content:center;padding-top:78px}
.feature{width:282px;text-align:center;padding:0 30px}
.feature+.feature{border-left:2px solid var(--teal)}
.feature svg{display:block;margin:0 auto 22px}
.feature h3{font-size:16px;line-height:24px;font-weight:700;margin-bottom:12px}
.feature p{font-size:13px;line-height:21px;color:var(--muted)}

/* skills */
.skills{height:407px;background:var(--skills);color:var(--white)}
.skills h2{left:85px;top:62px;font-size:30px;font-weight:700}
.skill{position:absolute;width:465px}
.skill h4{font-size:15px;font-weight:700;margin-bottom:10px}
.track{height:14px;background:var(--white);position:relative}
.fill{height:100%}
.pct{position:absolute;right:6px;top:0;font-size:10px;line-height:14px;color:#555}

/* rentals */
.rentals{height:459px}
.rentals-band{left:187px;top:0;width:128px;height:459px;background:var(--teal)}
.laptop{left:115px;top:95px;width:425px;height:285px;border-radius:12px 12px 4px 4px;background:linear-gradient(150deg,#e9eef1,#b8c4cc);box-shadow:0 8px 18px rgba(0,0,0,.2)}
.rentals h2{left:585px;top:78px;width:560px;font-size:29px;line-height:42px;font-weight:700}
.rent-list{left:585px;top:172px;display:grid;grid-template-columns:180px 230px 170px;row-gap:10px;list-style:none;font-size:12.5px;color:#44484e}
.rent-list li{display:flex;gap:8px;align-items:flex-start}
.rentals .link{left:585px;top:355px;color:var(--navy)}

/* testimonial */
.testimonial{height:456px;background:radial-gradient(circle at 60% 40%,#1e5a5a 0%,#0f3a3e 45%,#0a2529 100%);color:var(--white);text-align:center}
.avatar{left:555px;top:65px;width:90px;height:90px;border-radius:50%;background:linear-gradient(#c9a27e,#5b4030);border:4px solid var(--white)}
.quote{left:170px;top:175px;width:860px;font-size:19px;line-height:36px}
.qmark{font-family:Georgia,serif;font-size:40px;font-weight:700;position:absolute}
.author{left:0;width:1200px;top:335px;font-family:"Montserrat",sans-serif;font-weight:700;font-size:15px;letter-spacing:1px}
.role{left:0;width:1200px;top:362px;font-size:15px}

/* contact */
.contact{height:508px}
.contact h2{left:0;width:1200px;top:65px;text-align:center;font-size:30px;font-weight:700}
.field{position:absolute;border:1px solid var(--line);color:#a9adb3;font-size:12px;padding:14px 12px}
.btn-teal{position:absolute;left:530px;top:399px;width:140px;height:40px;background:var(--teal);color:var(--ink)}

/* footer */
.site-footer{height:349px;background:linear-gradient(180deg,#3c3f44,#2f3236);color:var(--white)}
.site-footer h4{font-size:13px;font-weight:700;position:absolute;top:68px;letter-spacing:.5px}
.foot-about{left:85px;top:110px;width:300px;font-size:12px;line-height:22px;color:#d3d5d8}
.foot-contact{left:500px;top:110px;font-size:12px;line-height:22px;color:#d3d5d8;list-style:none}
.foot-contact li{display:flex;gap:12px}
.subscribe{left:850px;top:105px;display:flex}
.subscribe div:first-child{width:200px;height:40px;border:1px solid #8a8e94;font-size:12px;color:#c7c9cc;padding:12px}
.subscribe div:last-child{width:48px;height:40px;background:#62666c;display:flex;align-items:center;justify-content:center}
.socials{left:850px;top:172px;display:flex;gap:10px}
.socials span{width:30px;height:30px;border:1px solid var(--white);border-radius:50%}
.foot-bottom{left:85px;right:85px;top:300px;display:flex;justify-content:space-between;font-size:12px;color:#d3d5d8}
.foot-bottom nav{display:flex;gap:24px}
</style>
</head>
<body>

<header class="hero">
  <div class="abs brand"><span class="brand-dot"></span><span class="brand-name">tarvio</span></div>
  <nav class="abs nav"><span>HOME</span><span>ABOUT</span><span>LEASING</span><span>FAQ</span><span>CONTACT</span></nav>
  <div class="abs nav-phone"><span class="ic"><svg width="14" height="14" viewBox="0 0 24 24"><path fill="#fff" d="M6.6 10.8a15 15 0 0 0 6.6 6.6l2.2-2.2c.3-.3.7-.4 1-.2 1.1.4 2.3.6 3.6.6.6 0 1 .4 1 1V20c0 .6-.4 1-1 1A17 17 0 0 1 3 4c0-.6.4-1 1-1h3.5c.6 0 1 .4 1 1 0 1.3.2 2.5.6 3.6.1.3 0 .7-.2 1z"/></svg></span>(555) 014-2290</div>
  <h1 class="abs hero-title">Our goal is <span>SIMPLE SAVE</span>Labs Time &amp; Money</h1>
  <span class="abs hero-more">LEARN MORE</span>
  <div class="abs hero-pager">
    <svg width="22" height="8" viewBox="0 0 22 8"><path d="M22 4H2M5 1 2 4l3 3" stroke="#fff" stroke-width="1.5" fill="none"/></svg>
    PREVIOUS &nbsp;|&nbsp; NEXT
    <svg width="22" height="8" viewBox="0 0 22 8"><path d="M0 4h20M17 1l3 3-3 3" stroke="#fff" stroke-width="1.5" fill="none"/></svg>
  </div>
  <div class="abs hero-frame"></div>
  <div class="abs hero-product" role="img" aria-label="White benchtop lab instrument with a sample cartridge inserted"></div>
</header>

<section class="contact-bar">
  <label>Contact Us</label>
  <div class="bar-field">Name</div>
  <div class="bar-field">Email</div>
  <div class="bar-field">Phone</div>
  <span class="btn btn-yellow">SUBMIT</span>
</section>

<section class="trusted">
  <div class="abs trusted-band"></div>
  <div class="abs trusted-photo" role="img" aria-label="Business partners shaking hands over a desk"></div>
  <h2 class="abs">Trusted Company Offering Scientific <span class="teal-text">Equipment Service</span> Plans and Flexible Leases</h2>
  <p class="abs">At tarvio, our goal is to ensure the success of your business. Whether you are running a laboratory or other scientific facilities, we want to keep you provided with the best in cutting-edge equipment. That's why we offer flexible scientific equipment leasing options with worry-free service plans- to provide your business with the tools needed to perform at its peak.</p>
  <span class="abs link">TAKE A TOUR</span>
</section>

<section class="understand">
  <svg class="abs donut" width="510" height="490" viewBox="0 0 510 490">
    <g transform="rotate(-90 255 245)" fill="none">
      <circle cx="255" cy="245" r="215" stroke="#8fd39a" stroke-width="26" stroke-dasharray="1130 221"/>
      <circle cx="255" cy="245" r="183" stroke="#22c7a4" stroke-width="26" stroke-dasharray="900 250"/>
      <circle cx="255" cy="245" r="151" stroke="#1b6e93" stroke-width="26" stroke-dasharray="720 229"/>
      <circle cx="255" cy="245" r="119" stroke="#174c7a" stroke-width="26" stroke-dasharray="560 188"/>
    </g>
    <circle cx="255" cy="245" r="96" fill="#0d2d5e"/>
    <text x="255" y="232" fill="#fff" font-family="Montserrat,sans-serif" font-size="15" font-weight="700" text-anchor="middle">We have</text>
    <text x="255" y="252" fill="#fff" font-family="Montserrat,sans-serif" font-size="15" font-weight="700" text-anchor="middle">you completely</text>
    <text x="255" y="272" fill="#fff" font-family="Montserrat,sans-serif" font-size="15" font-weight="700" text-anchor="middle">covered</text>
  </svg>
  <h2 class="abs">We Understand Your Needs Because We Are <span class="teal-text">Scientists First</span></h2>
  <p class="abs">When it comes to creating innovative solutions that cater to your lab, tarvio's dedicated team of problem-solvers has got you covered. Here's how we save you time and money:</p>
  <ul class="abs checks">
    <li><svg width="14" height="12" viewBox="0 0 14 12"><path d="M1 6l4 4 8-9" stroke="#22c7a4" stroke-width="2.5" fill="none"/></svg>We collaborate with you directly- no middlemen</li>
    <li><svg width="14" height="12" viewBox="0 0 14 12"><path d="M1 6l4 4 8-9" stroke="#22c7a4" stroke-width="2.5" fill="none"/></svg>We handle scientific equipment service, repairs, and maintenance</li>
    <li><svg width="14" height="12" viewBox="0 0 14 12"><path d="M1 6l4 4 8-9" stroke="#22c7a4" stroke-width="2.5" fill="none"/></svg>We consolidate and streamline the ancillary work associated with lab equipment procurement and service</li>
    <li><svg width="14" height="12" viewBox="0 0 14 12"><path d="M1 6l4 4 8-9" stroke="#22c7a4" stroke-width="2.5" fill="none"/></svg>We utilize our networks to bring you the most cost-savings possible</li>
    <li><svg width="14" height="12" viewBox="0 0 14 12"><path d="M1 6l4 4 8-9" stroke="#22c7a4" stroke-width="2.5" fill="none"/></svg>We improve cash flow by removing the upfront cost of purchasing, freeing up capital in your everyday budget</li>
    <li><svg width="14" height="12" viewBox="0 0 14 12"><path d="M1 6l4 4 8-9" stroke="#22c7a4" stroke-width="2.5" fill="none"/></svg>We may provide tax advantages with our lease structures</li>
  </ul>
  <span class="abs link">TAKE A TOUR</span>
</section>

<section class="cta">
  <span>Feel free to contact us if you have any questions or comments.</span>
  <span class="btn btn-yellow">CALL US NOW</span>
</section>

<section class="features">
  <div class="feature">
    <svg width="40" height="60" viewBox="0 0 40 60" fill="none" stroke="#2a8fc0" stroke-width="2.5"><path d="M8 2c0 18 24 20 24 28S8 42 8 58M32 2c0 18-24 20-24 28s24 12 24 28"/><path d="M12 10h16M12 50h16M14 20h12M14 40h12"/></svg>
    <h3>Worry free lab equipment PM/repair coverage.</h3>
    <p>Lorem ipsum is simply dummy text of the printing and typesetting industry. Lorem ipsum has been</p>
  </div>
  <div class="feature">
    <svg width="50" height="60" viewBox="0 0 50 60" fill="none" stroke="#2a8fc0" stroke-width="2.5"><path d="M18 4h12l-2 30H20zM24 34v12M10 56h30M14 46h20"/><circle cx="24" cy="12" r="3"/></svg>
    <h3>Cost-effective lease structures &amp; payment plans.</h3>
    <p>Lorem ipsum is simply dummy text of the printing and typesetting industry. Lorem ipsum has been</p>
  </div>
  <div class="feature">
    <svg width="56" height="60" viewBox="0 0 56 60" fill="none" stroke="#2a8fc0" stroke-width="2.5"><path d="M4 56h48M8 56V24M48 56V24M4 24h48M14 20V4h6v16M25 20V4h6v16M36 20V4h6v16"/><path d="M14 40h28"/></svg>
    <h3>Knowledge of the laboratory.</h3>
    <p>Lorem ipsum is simply dummy text of the printing and typesetting industry. Lorem ipsum has been</p>
  </div>
</section>

<section class="skills">
  <h2 class="abs">Our Skills</h2>
  <div class="skill" style="left:85px;top:137px"><h4>COST SAVING</h4><div class="track"><div class="fill" style="width:90%;background:var(--green)"></div><span class="pct">90%</span></div></div>
  <div class="skill" style="left:85px;top:212px"><h4>LEASE PLAN FLEXIBILITY</h4><div class="track"><div class="fill" style="width:80%;background:var(--blue)"></div><span class="pct">80%</span></div></div>
  <div class="skill" style="left:85px;top:287px"><h4>CUSTOMER SERVICE</h4><div class="track"><div class="fill" style="width:55%;background:var(--orange)"></div><span class="pct">55%</span></div></div>
  <div class="skill" style="left:612px;top:137px"><h4 style="font-size:17px">THE COMPETITION</h4></div>
  <div class="skill" style="left:612px;top:212px"><h4>RELIABILITY</h4><div class="track"><div class="fill" style="width:90%;background:var(--blue)"></div><span class="pct">90%</span></div></div>
  <div class="skill" style="left:612px;top:287px"><h4>CONTINUED SUPPORT</h4><div class="track"><div class="fill" style="width:55%;background:var(--orange)"></div><span class="pct">55%</span></div></div>
</section>

<section class="rentals">
  <div class="abs rentals-band"></div>
  <div class="abs laptop" role="img" aria-label="Laptop showing a video about equipment features with a play button"></div>
  <h2 class="abs">Our Fully Customized Rentals Include <span class="teal-text">New &amp; Refurbished</span> Options</h2>
  <ul class="abs rent-list">
    <li><svg width="12" height="10" viewBox="0 0 14 12"><path d="M1 6l4 4 8-9" stroke="#22c7a4" stroke-width="2.5" fill="none"/></svg>Autoclaves</li>
    <li><svg width="12" height="10" viewBox="0 0 14 12"><path d="M1 6l4 4 8-9" stroke="#22c7a4" stroke-width="2.5" fill="none"/></svg>Next Generation Sequencers</li>
    <li><svg width="12" height="10" viewBox="0 0 14 12"><path d="M1 6l4 4 8-9" stroke="#22c7a4" stroke-width="2.5" fill="none"/></svg>Clinical Chemistry Analyzers</li>
    <li><svg width="12" height="10" viewBox="0 0 14 12"><path d="M1 6l4 4 8-9" stroke="#22c7a4" stroke-width="2.5" fill="none"/></svg>Lab Balances</li>
    <li><svg width="12" height="10" viewBox="0 0 14 12"><path d="M1 6l4 4 8-9" stroke="#22c7a4" stroke-width="2.5" fill="none"/></svg>Flow Cytometers</li>
    <li><svg width="12" height="10" viewBox="0 0 14 12"><path d="M1 6l4 4 8-9" stroke="#22c7a4" stroke-width="2.5" fill="none"/></svg>Blood Bank Analyzers</li>
    <li><svg width="12" height="10" viewBox="0 0 14 12"><path d="M1 6l4 4 8-9" stroke="#22c7a4" stroke-width="2.5" fill="none"/></svg>Centrifuges</li>
    <li><svg width="12" height="10" viewBox="0 0 14 12"><path d="M1 6l4 4 8-9" stroke="#22c7a4" stroke-width="2.5" fill="none"/></svg>PCR Systems</li>
    <li><svg width="12" height="10" viewBox="0 0 14 12"><path d="M1 6l4 4 8-9" stroke="#22c7a4" stroke-width="2.5" fill="none"/></svg>Peptide Synthesizers</li>
    <li><svg width="12" height="10" viewBox="0 0 14 12"><path d="M1 6l4 4 8-9" stroke="#22c7a4" stroke-width="2.5" fill="none"/></svg>Microscopes</li>
    <li><svg width="12" height="10" viewBox="0 0 14 12"><path d="M1 6l4 4 8-9" stroke="#22c7a4" stroke-width="2.5" fill="none"/></svg>Liquid Handlers</li>
    <li><svg width="12" height="10" viewBox="0 0 14 12"><path d="M1 6l4 4 8-9" stroke="#22c7a4" stroke-width="2.5" fill="none"/></svg>Microarray Scanners</li>
    <li><svg width="12" height="10" viewBox="0 0 14 12"><path d="M1 6l4 4 8-9" stroke="#22c7a4" stroke-width="2.5" fill="none"/></svg>Cryostats</li>
    <li><svg width="12" height="10" viewBox="0 0 14 12"><path d="M1 6l4 4 8-9" stroke="#22c7a4" stroke-width="2.5" fill="none"/></svg>Microplate Readers</li>
  </ul>
  <span class="abs link">OUR SERVICES</span>
</section>

<section class="testimonial" role="img" aria-label="Dark teal backdrop of blurred laboratory molecules">
  <div class="abs avatar" role="img" aria-label="Portrait of the team member quoted"></div>
  <span class="qmark" style="left:195px;top:165px">“</span>
  <p class="abs quote">My time spent in the lab opened my eyes to the passion and dedication that drives scientists, as well as the frustration of a tight budget and equipment upkeep. tarvio was created in order to help overcome these obstacles and enable scientists to focus on what they're truly passionate about: research.</p>
  <span class="qmark" style="left:985px;top:280px">”</span>
  <div class="abs author">— DAN MORROW —</div>
  <div class="abs role">LAB RELATIONS</div>
</section>

<section class="contact">
  <h2 class="abs"><span class="teal-text">Contact</span> with us</h2>
  <div class="field" style="left:85px;top:129px;width:325px;height:45px">Name</div>
  <div class="field" style="left:435px;top:129px;width:325px;height:45px">Email</div>
  <div class="field" style="left:785px;top:129px;width:325px;height:45px">Phone</div>
  <div class="field" style="left:85px;top:189px;width:1025px;height:176px">Your Message</div>
  <span class="btn btn-teal">SUBMIT</span>
</section>

<footer class="site-footer">
  <h4 style="left:85px">ABOUT US</h4>
  <p class="abs foot-about">We are a team of Westbay University scientists driven by our passion for research. We strive to serve the scientific community. We love what we do, and who we work with. Together we can make positive changes in the world of research.</p>
  <h4 style="left:500px">CONTACT INFO</h4>
  <ul class="abs foot-contact">
    <li><svg width="12" height="16" viewBox="0 0 12 16"><path d="M6 1a5 5 0 0 1 5 5c0 4-5 9-5 9S1 10 1 6a5 5 0 0 1 5-5z" stroke="#fff" fill="none" stroke-width="1.3"/><circle cx="6" cy="6" r="1.8" fill="#fff"/></svg><span>tarvio Inc.<br>200 Alder Street, Suite 410<br>Oakland, CA 94607</span></li>
    <li style="margin-top:10px"><svg width="12" height="14" viewBox="0 0 24 24"><path fill="#fff" d="M6.6 10.8a15 15 0 0 0 6.6 6.6l2.2-2.2c.3-.3.7-.4 1-.2 1.1.4 2.3.6 3.6.6.6 0 1 .4 1 1V20c0 .6-.4 1-1 1A17 17 0 0 1 3 4c0-.6.4-1 1-1h3.5c.6 0 1 .4 1 1 0 1.3.2 2.5.6 3.6.1.3 0 .7-.2 1z"/></svg><span>(555) 014-2290<br>info@tarvio.com<br>https://tarvio.com</span></li>
  </ul>
  <h4 style="left:850px">STAY IN TOUCH</h4>
  <div class="abs subscribe"><div>Subscribe our newsletter</div><div><svg width="18" height="16" viewBox="0 0 18 16"><path d="M1 8 17 1l-4 14-4-5z" fill="#fff"/></svg></div></div>
  <div class="abs socials"><span></span><span></span><span></span><span></span></div>
  <div class="abs foot-bottom">
    <nav><span>Home</span><span>About</span><span>FAQ</span><span>Contact</span></nav>
    <span>Copyright © 2018 - tarvio</span>
  </div>
</footer>

</body>
</html>
```